Harborline Motors LLC

Car Dealer Customer Service
Address: 2741 Linden Avenue, Shelbyville, TN 37162
web: www.harborlinemotorstn.net
email: harborlinemotorstn@mailbox-example.net
Phone: (931) 555-0148
Phone: (629) 555-0173

```html
<!DOCTYPE html>
<html lang="en">
<head>
<meta charset="utf-8">
<title>Harborline Motors LLC — Business Card</title>
<link href="https://fonts.googleapis.com/css2?family=Poppins:wght@400;500;700;800&display=swap" rel="stylesheet">
<style>
  :root {
    --brand-blue: #2490c8;
    --brand-blue-deep: #1f78ac;
    --brand-yellow: #e8b03e;
    --ink: #151515;
    --paper: #f4f4f2;
    --backdrop: #e9e9e7;
  }
  * { box-sizing: border-box; margin: 0; padding: 0; }
  html, body {
    width: 1200px; height: 721px; overflow: hidden;
    background: var(--backdrop);
    font-family: "Poppins", sans-serif;
    color: var(--ink);
  }
  .stage {
    position: relative; width: 1200px; height: 721px;
    display: flex; align-items: center; justify-content: center; gap: 60px;
  }
  .card {
    position: relative; width: 500px; height: 286px;
    background: var(--paper); overflow: hidden;
    box-shadow: 0 10px 28px rgba(0,0,0,.14);
  }
  .card-art { position: absolute; inset: 0; width: 100%; height: 100%; }

  /* Front */
  .front-brand {
    position: absolute; inset: 0;
    display: flex; align-items: center; justify-content: center; gap: 12px;
  }
  .brand-dot {
    width: 22px; height: 22px; border-radius: 50%;
    background: var(--brand-blue-deep);
  }
  .brand-name {
    font-weight: 700; font-size: 26px; letter-spacing: .5px;
    text-transform: uppercase; color: var(--brand-blue-deep);
  }

  /* Back */
  .role {
    position: absolute; left: 34px; top: 34px;
    font-weight: 800; font-size: 15px; line-height: 1.15;
    text-transform: uppercase; letter-spacing: -.2px;
  }
  .divider {
    position: absolute; left: 34px; top: 88px; width: 200px;
    border-top: 1px solid var(--ink);
  }
  .contacts {
    position: absolute; left: 34px; top: 104px;
    list-style: none; font-size: 9.5px; line-height: 1.75;
    letter-spacing: 1px; text-transform: uppercase;
  }
  .contacts strong { font-weight: 700; }
  .back-brand {
    position: absolute; right: 30px; top: 118px;
    display: flex; align-items: center; gap: 8px;
  }
  .back-brand .brand-dot { width: 16px; height: 16px; }
  .back-brand .brand-name { font-size: 15px; }
  .address {
    position: absolute; right: 30px; bottom: 34px;
    font-size: 9.5px; line-height: 1.6; letter-spacing: 1px;
    text-transform: uppercase; text-align: right;
  }
</style>
</head>
<body>
<main class="stage">

  <section class="card card-back" aria-label="Business card, contact side">
    <svg class="card-art" viewBox="0 0 500 286" preserveAspectRatio="none" aria-hidden="true">
      <polygon points="0,266 200,266 190,286 0,286" fill="var(--brand-yellow)"/>
      <polygon points="200,266 500,266 500,286 190,286" fill="var(--brand-blue)"/>
    </svg>
    <h2 class="role">Car Dealer<br>Customer Service</h2>
    <div class="divider"></div>
    <ul class="contacts">
      <li><strong>Phone:</strong> (931) 555-0148</li>
      <li><strong>Phone:</strong> (629) 555-0173</li>
      <li>www.harborlinemotorstn.net</li>
      <li>harborlinemotorstn@mailbox-example.net</li>
    </ul>
    <div class="back-brand">
      <span class="brand-dot"></span>
      <span class="brand-name">Harborline Motors</span>
    </div>
    <p class="address">2741 Linden Avenue,<br>Shelbyville, TN 37162</p>
  </section>

  <section class="card card-front" aria-label="Business card, brand side">
    <svg class="card-art" viewBox="0 0 500 286" preserveAspectRatio="none" aria-hidden="true">
      <polygon points="0,0 150,0 60,286 0,286" fill="var(--brand-blue)"/>
      <polygon points="150,0 200,0 175,30 140,30" fill="var(--brand-yellow)"/>
      <polygon points="420,0 500,0 500,286 330,286" fill="var(--brand-yellow)"/>
      <polygon points="345,240 330,286 270,286 285,240" fill="var(--brand-blue)"/>
      <polygon points="130,40 400,40 360,250 90,250" fill="var(--paper)"/>
    </svg>
    <div class="front-brand">
      <span class="brand-dot"></span>
      <span class="brand-name">Harborline Motors</span>
    </div>
  </section>

</main>
</body>
</html>
```